Design a App to help people have successful dates!

We require an awesome designer to help us with an App design for a new dating app we are introducing! Our App is intended to help Users build confidence is knowing what questions or ask and answer when going on dates! As you can see from our Project Brief, the intent of the app is to display two types of content to the user 1) Dating Questions, and 2) Dating Tips. We have developed wireframes to help convey what each screen should convey. The intent is to 'inform' and 'educate' the User on what questions to ask, or what questions could be asked of them. Also, we would like to include Banner Ads on the 'Question' and 'Tip' screens, which you can see in the brief.

Target Market(s)

Men and women - aged 18 - 45 who need help identifying dating questions

Industry/Entity Type

Dating App

Font styles to use
Sans Serif

Requirements
Must have
• Please review the PDF brief that we have uploaded. Please make the swipe left and right feature modern (I only included the buttons as a guide only). The ‘Romance Prompt Ace’ App is intended to be a light-hearted, simple, elegant, fun App, to help Users ask and engage in dating questions. Think of this app as an 'LoveNest' (high quality, educated Users) to help users with identifying questions to ask on dates.
Nice to have
• Please review the PDF brief that we have uploaded.
Should not have
• The App is intended to only include genuine, legitimate, clean and appropriate content. This is not a 'Flarn' stiyle look-up app.

```html
<!DOCTYPE html>
<html lang="en">
<head>
<meta charset="utf-8">
<title>Romance Prompt Ace – App Screens</title>
<link href="https://fonts.googleapis.com/css2?family=Nunito:ital,wght@0,400;0,600;0,700;0,800;1,400&display=swap" rel="stylesheet">
<style>
  :root {
    --ink: #333333;
    --muted: #555555;
    --blue: #56b0e2;
    --blue-deep: #1f6fb0;
    --pink: #ff66b0;
    --beige: #e8e5c3;
    --beige-dash: #bdb98f;
    --heart: #ff1515;
    --white: #ffffff;
    --shadow: 0 3px 10px rgba(0,0,0,0.12);
  }
  * { box-sizing: border-box; margin: 0; padding: 0; }
  html, body { width: 1200px; height: 1200px; overflow: hidden; background: var(--white); }
  body { font-family: "Nunito", sans-serif; color: var(--ink); position: relative; }

  .screen { position: absolute; width: 346px; height: 586px; }
  .screen--a { left: 73px; }
  .screen--b { left: 420px; }
  .screen--c { left: 766px; }
  .row-top { top: 0; }
  .row-bottom { top: 586px; }

  /* header */
  .back { position: absolute; left: 57px; top: 87px; width: 10px; height: 14px; }
  .topbar { position: absolute; left: 0; width: 346px; top: 85px; text-align: center; line-height: 1.25; }
  .topbar__city { font-size: 8.5px; font-weight: 700; color: var(--ink); }
  .topbar__date { font-size: 7px; color: var(--muted); }
  .topbar__mark { position: absolute; left: 272px; top: 86px; width: 12px; height: 12px; border-radius: 50%; background: var(--pink); }

  /* welcome */
  .brand-mark { position: absolute; left: 124px; top: 168px; width: 98px; height: 98px; border-radius: 50%; background: var(--pink); }
  .brand-name { position: absolute; left: 0; width: 346px; top: 297px; text-align: center; font-size: 15px; font-weight: 800; }
  .brand-tagline { position: absolute; left: 0; width: 346px; top: 324px; text-align: center; font-size: 12.5px; font-style: italic; color: var(--muted); }
  .cta { position: absolute; left: 86px; top: 472px; width: 187px; height: 30px; background: var(--white); border-radius: 4px; box-shadow: var(--shadow); font-size: 12.5px; font-weight: 800; display: flex; align-items: center; justify-content: center; }

  /* menu cards */
  .menu-card { position: absolute; left: 78px; width: 185px; height: 147px; background: var(--white); border-radius: 10px; box-shadow: var(--shadow); }
  .menu-card--questions { top: 150px; }
  .menu-card--tips { top: 341px; }
  .menu-card__art { position: absolute; left: 42px; top: 16px; width: 102px; height: 92px; border-radius: 10px; background: linear-gradient(160deg, var(--beige) 0%, #2bb3e8 45%, #08a7e3 100%); }
  .menu-card__label { position: absolute; left: 0; width: 185px; bottom: 12px; text-align: center; font-size: 13px; font-weight: 800; }

  /* question bubble */
  .question { position: absolute; left: 77px; top: 190px; width: 200px; height: 155px; }
  .question svg { position: absolute; left: 0; top: 0; }
  .question__text { position: absolute; left: 8px; top: 8px; width: 178px; height: 100px; display: flex; align-items: center; justify-content: center; text-align: center; font-size: 14.5px; font-weight: 600; line-height: 1.35; color: var(--ink); }

  /* tip */
  .tip-body { position: absolute; left: 92px; top: 234px; width: 194px; height: 166px; background: var(--beige); border-radius: 10px; box-shadow: var(--shadow); padding: 26px 14px 0 25px; font-size: 11px; line-height: 16px; color: var(--ink); }
  .tip-body--compact { font-size: 10px; line-height: 13.7px; padding-top: 28px; }
  .tip-body::after { content: ""; position: absolute; inset: 7px; border: 1px dashed var(--beige-dash); border-radius: 7px; pointer-events: none; }
  .tip-title { position: absolute; left: 57px; top: 141px; width: 192px; height: 116px; background: var(--blue); border-radius: 10px; box-shadow: var(--shadow); display: flex; align-items: center; justify-content: center; text-align: center; padding: 0 22px; color: var(--white); font-size: 14.5px; font-weight: 600; line-height: 1.35; }
  .tip-title::after { content: ""; position: absolute; inset: 7px; border: 1.5px dashed var(--blue-deep); border-radius: 7px; }

  .fav { position: absolute; width: 26px; height: 24px; }
  .fav--question { left: 248px; top: 183px; }
  .fav--tip { left: 224px; top: 131px; }

  /* swipe controls */
  .swipe { position: absolute; top: 425px; width: 52px; height: 52px; border-radius: 50%; background: var(--white); box-shadow: var(--shadow); display: flex; align-items: center; justify-content: center; }
  .swipe--prev { left: 62px; }
  .swipe--next { left: 235px; }
  .swipe svg { width: 28px; height: 28px; }

  .ad-banner { position: absolute; left: 69px; top: 500px; width: 210px; height: 36px; background: linear-gradient(90deg, #3a4b5c 0%, #8a6a3a 40%, #5a4a3a 70%, #d8c89a 100%); }
</style>
</head>
<body>
  <svg width="0" height="0" style="position:absolute">
    <defs>
      <path id="heart-shape" d="M13 22 C5 16 1.5 12 1.5 7.5 C1.5 4 4 1.5 7.2 1.5 C9.6 1.5 11.6 3 13 5 C14.4 3 16.4 1.5 18.8 1.5 C22 1.5 24.5 4 24.5 7.5 C24.5 12 21 16 13 22 Z"/>
      <path id="reply-shape" d="M11 4 L2 11.5 L11 19 V14.2 C17 14 21 16 24.5 21 C23.5 13.5 19 9 11 8.8 Z"/>
      <polyline id="chevron" points="8,2 3,7 8,12" fill="none" stroke-width="1.8" stroke-linecap="round" stroke-linejoin="round"/>
    </defs>
  </svg>

  <!-- Welcome -->
  <section class="screen screen--a row-top">
    <div class="brand-mark"></div>
    <h1 class="brand-name">Romance Prompt Ace</h1>
    <p class="brand-tagline">No awkward silences</p>
    <div class="cta">Get started!</div>
  </section>

  <!-- Menu -->
  <section class="screen screen--b row-top">
    <svg class="back" viewBox="0 0 10 14"><use href="#chevron" stroke="var(--blue)"/></svg>
    <div class="topbar"><div class="topbar__city">San Francisco</div><div class="topbar__date">26 July 6:26am</div></div>
    <div class="topbar__mark"></div>
    <div class="menu-card menu-card--questions">
      <div class="menu-card__art" role="img" aria-label="Illustration of a blue speech card with a question mark"></div>
      <div class="menu-card__label">Dating Questions</div>
    </div>
    <div class="menu-card menu-card--tips">
      <div class="menu-card__art" role="img" aria-label="Illustration of a blue card with a light bulb"></div>
      <div class="menu-card__label">Dating Tips</div>
    </div>
  </section>

  <!-- Question 1 -->
  <section class="screen screen--c row-top">
    <svg class="back" viewBox="0 0 10 14"><use href="#chevron" stroke="var(--blue)"/></svg>
    <div class="topbar"><div class="topbar__city">San Francisco</div><div class="topbar__date">26 July 6:26am</div></div>
    <div class="question">
      <svg width="200" height="155" viewBox="0 0 200 155">
        <path d="M10 2 H184 Q194 2 194 12 V108 Q194 118 184 118 H148 L114 152 L125 118 H10 Q0 118 0 108 V12 Q0 2 10 2 Z" fill="var(--beige)"/>
        <rect x="8" y="10" width="178" height="100" rx="6" fill="none" stroke="var(--beige-dash)" stroke-dasharray="4 3"/>
      </svg>
      <div class="question__text">What makes you laugh?</div>
    </div>
    <svg class="fav fav--question" viewBox="0 0 26 24"><use href="#heart-shape" fill="var(--white)" stroke="var(--heart)" stroke-width="2.4"/></svg>
    <div class="swipe swipe--prev"><svg viewBox="0 0 26 24"><use href="#reply-shape" fill="var(--blue)"/></svg></div>
    <div class="swipe swipe--next"><svg viewBox="0 0 26 24"><g transform="translate(26 0) scale(-1 1)"><use href="#reply-shape" fill="var(--pink)"/></g></svg></div>
    <div class="ad-banner" role="img" aria-label="Game advertisement banner"></div>
  </section>

  <!-- Question 2 -->
  <section class="screen screen--a row-bottom">
    <svg class="back" viewBox="0 0 10 14"><use href="#chevron" stroke="var(--blue)"/></svg>
    <div class="topbar"><div class="topbar__city">San Francisco</div><div class="topbar__date">26 July 6:26am</div></div>
    <div class="question">
      <svg width="200" height="155" viewBox="0 0 200 155">
        <path d="M10 2 H184 Q194 2 194 12 V108 Q194 118 184 118 H148 L114 152 L125 118 H10 Q0 118 0 108 V12 Q0 2 10 2 Z" fill="var(--beige)"/>
        <rect x="8" y="10" width="178" height="100" rx="6" fill="none" stroke="var(--beige-dash)" stroke-dasharray="4 3"/>
      </svg>
      <div class="question__text">What does your perfect weekend look like?</div>
    </div>
    <svg class="fav fav--question" viewBox="0 0 26 24"><use href="#heart-shape" fill="var(--heart)"/></svg>
    <div class="swipe swipe--prev"><svg viewBox="0 0 26 24"><use href="#reply-shape" fill="var(--blue)"/></svg></div>
    <div class="swipe swipe--next"><svg viewBox="0 0 26 24"><g transform="translate(26 0) scale(-1 1)"><use href="#reply-shape" fill="var(--pink)"/></g></svg></div>
    <div class="ad-banner" role="img" aria-label="Game advertisement banner"></div>
  </section>

  <!-- Tip 1 -->
  <section class="screen screen--b row-bottom">
    <svg class="back" viewBox="0 0 10 14"><use href="#chevron" stroke="var(--blue)"/></svg>
    <div class="topbar"><div class="topbar__city">San Francisco</div><div class="topbar__date">26 July 6:26am</div></div>
    <div class="tip-body">Don’t be one of those ‘fashionable late’ people. Your date may feel nervous or anxious whether you are even coming. Make sure you arrive to meet your date on time,</div>
    <div class="tip-title">Arrive to the date on time.</div>
    <svg class="fav fav--tip" viewBox="0 0 26 24"><use href="#heart-shape" fill="var(--heart)"/></svg>
    <div class="swipe swipe--prev"><svg viewBox="0 0 26 24"><use href="#reply-shape" fill="var(--blue)"/></svg></div>
    <div class="swipe swipe--next"><svg viewBox="0 0 26 24"><g transform="translate(26 0) scale(-1 1)"><use href="#reply-shape" fill="var(--pink)"/></g></svg></div>
    <div class="ad-banner" role="img" aria-label="Game advertisement banner"></div>
  </section>

  <!-- Tip 2 -->
  <section class="screen screen--c row-bottom">
    <svg class="back" viewBox="0 0 10 14"><use href="#chevron" stroke="var(--blue)"/></svg>
    <div class="topbar"><div class="topbar__city">San Francisco</div><div class="topbar__date">26 July 6:26am</div></div>
    <div class="tip-body tip-body--compact">A great conversation is one where both parties feel engaged and are equally contributing. When your date shares something about themselves or asks you a question, always reply by sharing a similar story or asking them the same question.</div>
    <div class="tip-title">Keep the conversation equal.</div>
    <svg class="fav fav--tip" viewBox="0 0 26 24"><use href="#heart-shape" fill="var(--white)" stroke="var(--heart)" stroke-width="2.4"/></svg>
    <div class="swipe swipe--prev"><svg viewBox="0 0 26 24"><use href="#reply-shape" fill="var(--blue)"/></svg></div>
    <div class="swipe swipe--next"><svg viewBox="0 0 26 24"><g transform="translate(26 0) scale(-1 1)"><use href="#reply-shape" fill="var(--pink)"/></g></svg></div>
    <div class="ad-banner" role="img" aria-label="Game advertisement banner"></div>
  </section>
</body>
</html>
```